Wohnhof am Weiher - Zeitungsinserat für den Verkauf von Eigentumswohnungen

Wir brauchen ein Zeitungsinserat in zwei Formaten. Einmal 296 Breite x 440 Höhe mm und einmal 296 Breite x 220 mm Höhe.
Als Basis dient der sehr grobe Entwurf im Powerpoint (Entwurf.pptx).
Auf dem Entwurf fehlen noch die Kontaktangeben:
Brunnhofer Liegenschaften AG
Seematteweg 14
4387 Tannried
079 462 37 58
rbrunnhofer@tessin-ostwald.ch

Zudem muss noch der Link auf die Webseite aufgeführt werden.
www.wohnhof-am-weiher.ch

Zudem fehlt noch der Text:
Fordern Sie noch heute die Verkaufsunterlagen gedruckt oder per Email an. Schreiben Sie uns einfach eine Chatpost mit Ihrer Adresse.

Ich habe noch Files von den Innenvisualisierungen, den Aussenvisualisierungen sowie unser Logo hinzugefügt. Zudem habe ich Ihnen die Verkaufsbrochure angefügt. Sie können die Daten vom Entwurf gerne ergänzen wenn Ihnen etwas gefällt. Schön wäre es, wenn Sie den Stil ähnlich machen würden wie die Brochure.

Target Market(s)

Famillien, Paare und Rentner

Font styles to use
Serif

Colors

Designer to choose colors to be used in the design.

Requirements
Must have
• Tolles Design das sofort anspricht!

```html
<!DOCTYPE html>
<html lang="de">
<head>
<meta charset="utf-8">
<title>Wohnhof am Weiher – Inserate</title>
<link href="https://fonts.googleapis.com/css2?family=Open+Sans:wght@400;600;700&display=swap" rel="stylesheet">
<style>
:root{
  --blue:#1a8be0;
  --red:#d3121b;
  --gray-dark:#6a6a6a;
  --gray-light:#cdcdcd;
  --ink:#3a3a3a;
  --logo:#1d5f82;
  --white:#fff;
  --bg:#000;
}
*{box-sizing:border-box;margin:0;padding:0}
html,body{width:1200px;height:2640px;overflow:hidden;background:var(--bg);font-family:"Open Sans",Arial,sans-serif;color:var(--ink)}
.ad{position:absolute;background:var(--white);overflow:hidden}
.abs{position:absolute}
.photo{position:absolute}
.ph-outdoor{background:linear-gradient(180deg,#b9cfe0 0%,#dfe6ea 38%,#c8cfd2 55%,#7fa25a 75%,#5f8a3c 100%)}
.ph-outdoor-fade{background:linear-gradient(180deg,#e9edf0 0%,#f1f2f3 55%,#dfe3df 100%)}
.ph-interior{background:linear-gradient(160deg,#f1eeea 0%,#d9d5cf 60%,#b9b2a8 100%)}
.ph-aerial{background:linear-gradient(180deg,#c9d6de 0%,#7f9a6c 35%,#9aa884 60%,#6f8b4f 100%)}
.ph-blue{background:linear-gradient(180deg,#3a9be6 0%,#1a7fd0 60%,#1a6fbf 100%)}
.title-box{position:absolute;background:var(--blue);color:var(--white)}
.title-box h1{font-weight:700;line-height:1.05}
.title-box p{font-weight:400}
.feature{position:absolute}
.feature svg{position:absolute;left:0;top:0}
.feature h3{color:var(--blue);font-weight:700}
.feature p{line-height:1.2}
.logo-name{position:absolute;color:var(--logo);font-weight:700;text-align:center;line-height:1.15}
.request{position:absolute;line-height:1.3}
.footer{position:absolute;left:0;bottom:0;background:var(--blue);color:var(--white);font-weight:600;display:flex;align-items:center;white-space:nowrap}
.footer .web{position:absolute;right:0;top:0;bottom:0;background:var(--red);display:flex;align-items:center;justify-content:center;font-weight:700}
.footer .item{display:flex;align-items:center;gap:7px}
/* landscape table */
.l-house{position:absolute;left:455px;width:531px;border-top:2px solid var(--white)}
.l-house .tag{position:absolute;left:0;top:0;bottom:0;width:29px;background:var(--blue);color:var(--white);font-weight:700;font-size:13px;letter-spacing:3px;writing-mode:vertical-rl;transform:rotate(180deg);text-align:center}
.l-house .labels{position:absolute;left:29px;top:0;bottom:0;width:104px;background:var(--gray-dark)}
.l-row{position:absolute;left:0;right:0;display:flex;font-size:8px;line-height:1.15}
.l-row .lab{width:133px;padding-left:35px;color:var(--white);font-weight:600;white-space:nowrap}
.l-row .c1{width:62px;padding-left:14px;white-space:nowrap}
.l-row .c2{width:82px;white-space:nowrap}
.l-row .c3{width:172px}
.l-row .c4{width:74px;text-align:right;white-space:nowrap}
/* portrait table */
.p-head{position:absolute;left:0;width:142px;height:30px;background:var(--blue);color:var(--white);font-weight:700;font-size:21px;letter-spacing:5px;display:flex;align-items:center;justify-content:center}
.p-row{position:absolute;left:0;display:flex;font-size:13px;line-height:1.1}
.p-row .lab{width:142px;padding-left:18px;font-weight:600;color:#3a3a3a;position:relative;white-space:nowrap}
.p-row .lab::before{content:"";position:absolute;left:10px;top:4px;width:6px;height:6px;background:var(--blue)}
.p-row .data{display:flex;border-bottom:1px solid #bbb;margin-left:16px;padding-bottom:4px;width:530px}
.p-row .c1{width:86px;white-space:nowrap}
.p-row .c2{width:140px;white-space:nowrap}
.p-row .c3{width:200px}
.p-row .c4{width:104px;text-align:right;white-space:nowrap}
</style>
</head>
<body>

<section class="ad ad-landscape" style="left:107px;top:169px;width:986px;height:733px">
  <div class="photo ph-outdoor" style="left:0;top:0;width:588px;height:310px" role="img" aria-label="Aussenvisualisierung der Wohnanlage mit Gärten und Bäumen"></div>
  <div class="abs" style="left:0;top:0;width:12px;height:100px;background:var(--red)"></div>
  <div class="title-box" style="left:13px;top:42px;width:368px;height:58px;padding:5px 0 0 16px">
    <h1 style="font-size:30px">Wohnhof am Weiher</h1>
    <p style="font-size:14.5px">Hochwertige und moderne Eigentumswohnungen</p>
  </div>
  <div class="photo ph-blue" style="left:588px;top:0;width:204px;height:299px" role="img" aria-label="Blau getönte Ansicht der Wohnanlage"></div>
  <div class="abs" style="left:792px;top:0;width:194px;height:299px;background:var(--gray-dark)"></div>
  <div class="photo ph-interior" style="left:730px;top:16px;width:242px;height:127px;border:2px solid #fff" role="img" aria-label="Innenvisualisierung Wohnzimmer"></div>
  <div class="photo ph-interior" style="left:730px;top:157px;width:242px;height:127px;border:2px solid #fff" role="img" aria-label="Innenvisualisierung Küche und Essbereich"></div>
  <p class="request" style="left:600px;top:20px;width:118px;font-size:9.5px;font-weight:600;color:#fff">Fordern Sie noch heute die Verkaufsunterlagen gedruckt oder per Email an. Schreiben Sie uns einfach eine Chatpost mit Ihrer Adresse.</p>
  <div class="photo ph-aerial" style="left:233px;top:301px;width:209px;height:130px;border:2px solid #fff" role="img" aria-label="Luftaufnahme des Dorfes mit Hügeln"></div>

  <div class="feature" style="left:13px;top:359px;width:210px">
    <svg width="26" height="26" viewBox="0 0 26 26"><circle cx="13" cy="13" r="11.5" fill="none" stroke="#1a8be0" stroke-width="1.8"/><path d="M7.5 13.5l4 4 7-8" fill="none" stroke="#1a8be0" stroke-width="2"/></svg>
    <div style="margin-left:36px"><h3 style="font-size:11px">Bus und Bahn</h3><p style="font-size:9px">Der Bahnhof von Seewil mit Zugverbindungen nach Basel (20 Minuten) und Delemont ist in wenigen Minuten mit dem Bus zu erreichen.</p></div>
  </div>
  <div class="feature" style="left:13px;top:445px;width:220px">
    <svg width="26" height="26" viewBox="0 0 26 26"><circle cx="13" cy="13" r="11.5" fill="none" stroke="#1a8be0" stroke-width="1.8"/><path d="M7.5 13.5l4 4 7-8" fill="none" stroke="#1a8be0" stroke-width="2"/></svg>
    <div style="margin-left:36px"><h3 style="font-size:11px">Basel - Stadt</h3><p style="font-size:9px">Der nahegelegene Bahnhof in Seewil verfügt über sehr gute Verbindungen nach Basel (20 Minuten), welche durch den Doppelspurausbau in den kommenden Jahren sogar noch weiter verbessert werden.</p></div>
  </div>
  <div class="feature" style="left:13px;top:549px;width:210px">
    <svg width="26" height="26" viewBox="0 0 26 26"><circle cx="13" cy="13" r="11.5" fill="none" stroke="#1a8be0" stroke-width="1.8"/><path d="M7.5 13.5l4 4 7-8" fill="none" stroke="#1a8be0" stroke-width="2"/></svg>
    <div style="margin-left:36px"><h3 style="font-size:11px">Autobahn</h3><p style="font-size:9px">Die Wohnsiedlung ist ideal auch für den Individualverkehr erschlossen. Die Entfernung zur Autobahn J18 beträgt 12km und ist über Eschbach innerhalb von 15 Minuten erreichbar.</p></div>
  </div>
  <div class="feature" style="left:233px;top:455px;width:212px">
    <svg width="26" height="26" viewBox="0 0 26 26"><circle cx="13" cy="13" r="11.5" fill="none" stroke="#1a8be0" stroke-width="1.8"/><path d="M7.5 13.5l4 4 7-8" fill="none" stroke="#1a8be0" stroke-width="2"/></svg>
    <div style="margin-left:32px"><h3 style="font-size:11px">Einkaufen und weitere Dienstleistungen</h3><p style="font-size:9px">Durch die Nähe der Gemeindegrenze zwischen Seewil und Tannried liegen die Dorfzentren mit ihren Einkaufsmöglichkeiten (z.B. Auen Center sowie der Altstadt in Seewil) und Dienstleistungsangeboten in max. 2 Minuten Fahrtzeit oder in 10-15 Minuten Gehdistanz.</p></div>
  </div>
  <div class="feature" style="left:233px;top:585px;width:212px">
    <svg width="26" height="26" viewBox="0 0 26 26"><circle cx="13" cy="13" r="11.5" fill="none" stroke="#1a8be0" stroke-width="1.8"/><path d="M7.5 13.5l4 4 7-8" fill="none" stroke="#1a8be0" stroke-width="2"/></svg>
    <div style="margin-left:32px"><h3 style="font-size:11px">Erholung im Grünen</h3><p style="font-size:9px">Tannried erfüllt mit seinen Wäldern, dem eigenen «Dorfberg» dem «Stürmenkopf», den offenen Feldern, den Wander- und Velorouten und der ländlichen Ruhe alle Voraussetzungen, die ein Naherholungsgebiet begehrt machen.</p></div>
  </div>
  <div class="logo-name" style="left:30px;top:655px;width:200px;font-size:13px">Brunnhofer<br>Liegenschaften AG</div>
  <div class="abs" style="left:265px;top:686px;font-size:7px">Icons by Pixelhain from iconfeld.net</div>

  <div class="l-house" style="top:299px;height:132px">
    <div class="labels"></div><div class="tag">HAUS A</div>
    <div class="l-row" style="top:14px"><span class="lab">Attika Wohnung</span><span class="c1">4.5 Zimmer</span><span class="c2">108 m2 Wohnfläche</span><span class="c3">105 m2 grosse Sonnenterrasse</span><span class="c4">945'000 CHF</span></div>
    <div class="l-row" style="top:33px"><span class="lab">Obergeschoss</span><span class="c1">3.5 Zimmer</span><span class="c2">81 m2 Wohnfläche</span><span class="c3">16 m2 grosser Balkon</span><span class="c4">754'800 CHF</span></div>
    <div class="l-row" style="top:52px"><span class="lab">Obergeschoss</span><span class="c1">4.5 Zimmer</span><span class="c2">102 m2 Wohnfläche</span><span class="c3">33 m2 grosser Balkon</span><span class="c4">640'000 CHF</span></div>
    <div class="l-row" style="top:71px"><span class="lab">Erdgeschoss</span><span class="c1">3.5 Zimmer</span><span class="c2">81 m2 Wohnfläche</span><span class="c3">16 m2 gedeckter Sitzplatz und<br>über 120 m² Garten</span><span class="c4" style="padding-top:9px">657'000 CHF</span></div>
    <div class="l-row" style="top:100px"><span class="lab">Erdgeschoss</span><span class="c1">4.5 Zimmer</span><span class="c2">102 m2 Wohnfläche</span><span class="c3">33 m2 gedeckter Sitzplatz und<br>über 120 m² Garten</span><span class="c4" style="padding-top:9px">765'000 CHF</span></div>
  </div>
  <div class="l-house" style="top:431px;height:134px">
    <div class="labels"></div><div class="tag">HAUS B</div>
    <div class="l-row" style="top:14px"><span class="lab">Attika Wohnung</span><span class="c1">4.5 Zimmer</span><span class="c2">109 m2 Wohnfläche</span><span class="c3">107 m2 grosse Sonnenterrasse</span><span class="c4">965'000 CHF</span></div>
    <div class="l-row" style="top:33px"><span class="lab">Obergeschoss</span><span class="c1">2.5 Zimmer</span><span class="c2">69 m2 Wohnfläche</span><span class="c3">14 m2 grosse Balkon</span><span class="c4">550'000 CHF</span></div>
    <div class="l-row" style="top:52px"><span class="lab">Obergeschoss</span><span class="c1">4.5 Zimmer</span><span class="c2">117 m2 Wohnfläche</span><span class="c3">42 m2 grosse Balkon</span><span class="c4">877'500 CHF</span></div>
    <div class="l-row" style="top:71px"><span class="lab">Erdgeschoss</span><span class="c1">2.5 Zimmer</span><span class="c2">69 m2 Wohnfläche</span><span class="c3">14 m2 gedeckter Sitzplatz und<br>über 70 m² Garten</span><span class="c4" style="padding-top:9px">560'000 CHF</span></div>
    <div class="l-row" style="top:100px"><span class="lab">Erdgeschoss</span><span class="c1">4.5 Zimmer</span><span class="c2">117 m2 Wohnfläche</span><span class="c3">42 m2 gedeckter Sitzplatz und<br>über 140 m² Garten</span><span class="c4" style="padding-top:9px">889'000 CHF</span></div>
  </div>
  <div class="l-house" style="top:565px;height:132px">
    <div class="labels"></div><div class="tag">HAUS C</div>
    <div class="l-row" style="top:14px"><span class="lab">Attika Wohnung</span><span class="c1">4.5 Zimmer</span><span class="c2">129 m2 Wohnfläche</span><span class="c3">132 m2 grosse Sonnenterrasse</span><span class="c4">1'125'000 CHF</span></div>
    <div class="l-row" style="top:33px"><span class="lab">Obergeschoss</span><span class="c1">5.5 Zimmer</span><span class="c2">143 m2 Wohnfläche</span><span class="c3">43 m2 grosser Balkon</span><span class="c4">1'058'000 CHF</span></div>
    <div class="l-row" style="top:52px"><span class="lab">Obergeschoss</span><span class="c1">3.5 Zimmer</span><span class="c2">96 m2 Wohnfläche</span><span class="c3">23 m2 grosser Balkon</span><span class="c4">730'000 CHF</span></div>
    <div class="l-row" style="top:71px"><span class="lab">Erdgeschoss</span><span class="c1">5.5 Zimmer</span><span class="c2">143 m2 Wohnfläche</span><span class="c3">43 m2 gedeckter Sitzplatz und<br>über 120 m² Garten</span><span class="c4" style="padding-top:9px">1'065'000 CHF</span></div>
    <div class="l-row" style="top:100px"><span class="lab">Erdgeschoss</span><span class="c1">3.5 Zimmer</span><span class="c2">96 m2 Wohnfläche</span><span class="c3">23 m2 gedeckter Sitzplatz und<br>über 60 m² Garten</span><span class="c4" style="padding-top:9px">740'000 CHF</span></div>
  </div>

  <div class="footer" style="width:986px;height:36px;font-size:10px;padding-left:30px">
    <span style="width:210px">BRUNNHOFER LIEGENSCHAFTEN AG</span>
    <span class="item" style="width:215px"><svg width="13" height="15" viewBox="0 0 13 15"><rect width="13" height="15" rx="2" fill="#fff"/><circle cx="6.5" cy="6" r="2.5" fill="#1a8be0"/></svg>Seematteweg 14, 4387 Tannried</span>
    <span class="item" style="width:110px"><svg width="13" height="13" viewBox="0 0 13 13"><rect width="13" height="13" rx="2" fill="#fff"/><path d="M3.5 3c1 3 3 5.5 6 6.5l1-1.5-2-1-1 .8c-1-.6-1.8-1.4-2.3-2.4l.8-1-1-2z" fill="#1a8be0"/></svg>079 462 37 58</span>
    <span class="item"><svg width="13" height="13" viewBox="0 0 13 13"><rect width="13" height="13" rx="2" fill="#fff"/><path d="M3 4h7v5H3zM3 4l3.5 3L10 4" fill="none" stroke="#1a8be0" stroke-width="1"/></svg>rbrunnhofer@tessin-ostwald.ch</span>
    <span class="web" style="width:194px;font-size:12.5px">www.wohnhof-am-weiher.ch</span>
  </div>
</section>

<section class="ad ad-portrait" style="left:107px;top:1003px;width:980px;height:1457px">
  <div class="photo ph-outdoor" style="left:0;top:0;width:706px;height:383px" role="img" aria-label="Aussenvisualisierung der Wohnanlage mit Radfahrer und Bäumen"></div>
  <div class="photo ph-outdoor-fade" style="left:706px;top:0;width:274px;height:383px" role="img" aria-label="Verblasste Fortsetzung der Aussenansicht"></div>
  <div class="abs" style="left:360px;top:41px;width:12px;height:84px;background:var(--red)"></div>
  <div class="title-box" style="left:372px;top:41px;width:608px;height:84px;padding:6px 0 0 84px">
    <h1 style="font-size:46px">Wohnhof am Weiher</h1>
    <p style="font-size:22px">Hochwertige und moderne Eigentumswohnungen</p>
  </div>
  <div class="abs" style="left:18px;top:477px;width:665px;height:101px;background:var(--blue)"></div>
  <div class="abs" style="left:36px;top:477px;width:629px;height:80px;background:var(--white)"></div>
  <div class="photo ph-interior" style="left:34px;top:385px;width:312px;height:172px" role="img" aria-label="Innenvisualisierung Wohn- und Essbereich"></div>
  <div class="photo ph-interior" style="left:358px;top:385px;width:312px;height:172px" role="img" aria-label="Innenvisualisierung Küche"></div>

  <div class="abs" style="left:706px;top:383px;width:274px;height:1026px;background:var(--blue)"></div>
  <div class="photo ph-aerial" style="left:727px;top:403px;width:238px;height:174px;border:3px solid #fff" role="img" aria-label="Luftaufnahme des Dorfes mit Hügeln"></div>

  <div class="feature" style="left:727px;top:658px;width:240px;color:#fff">
    <svg width="24" height="24" viewBox="0 0 24 24"><circle cx="12" cy="12" r="10.5" fill="none" stroke="#fff" stroke-width="1.8"/><path d="M7 12.5l3.5 3.5 6.5-7.5" fill="none" stroke="#fff" stroke-width="2"/></svg>
    <div style="margin-left:34px"><h3 style="font-size:17px;color:#fff">Bus und Bahn</h3><p style="font-size:12.5px">Der Bahnhof von Seewil mit Zugverbindungen nach Basel (20 Minuten) und Delemont ist in wenigen Minuten mit dem Bus zu erreichen.</p></div>
  </div>
  <div class="feature" style="left:727px;top:769px;width:240px;color:#fff">
    <svg width="24" height="24" viewBox="0 0 24 24"><circle cx="12" cy="12" r="10.5" fill="none" stroke="#fff" stroke-width="1.8"/><path d="M7 12.5l3.5 3.5 6.5-7.5" fill="none" stroke="#fff" stroke-width="2"/></svg>
    <div style="margin-left:34px"><h3 style="font-size:17px;color:#fff">Basel - Stadt</h3><p style="font-size:12.5px">Der nahegelegene Bahnhof in Seewil verfügt über sehr gute Verbindungen nach Basel (20 Minuten), welche durch den Doppelspurausbau in den kommenden Jahren sogar noch weiter verbessert werden.</p></div>
  </div>
  <div class="feature" style="left:727px;top:907px;width:240px;color:#fff">
    <svg width="24" height="24" viewBox="0 0 24 24"><circle cx="12" cy="12" r="10.5" fill="none" stroke="#fff" stroke-width="1.8"/><path d="M7 12.5l3.5 3.5 6.5-7.5" fill="none" stroke="#fff" stroke-width="2"/></svg>
    <div style="margin-left:34px"><h3 style="font-size:17px;color:#fff">Autobahn</h3><p style="font-size:12.5px">Die Wohnsiedlung ist ideal auch für den Individualverkehr erschlossen. Die Entfernung zur Autobahn J18 beträgt 12km und ist über Eschbach innerhalb von 15 Minuten erreichbar.</p></div>
  </div>
  <div class="feature" style="left:727px;top:1030px;width:244px;color:#fff">
    <svg width="24" height="24" viewBox="0 0 24 24"><circle cx="12" cy="12" r="10.5" fill="none" stroke="#fff" stroke-width="1.8"/><path d="M7 12.5l3.5 3.5 6.5-7.5" fill="none" stroke="#fff" stroke-width="2"/></svg>
    <div style="margin-left:34px"><h3 style="font-size:17px;color:#fff;line-height:1.1">Einkaufen und weitere Dienstleistungen</h3><p style="font-size:12.5px">Durch die Nähe der Gemeindegrenze zwischen Seewil und Tannried liegen die Dorfzentren mit ihren Einkaufsmöglichkeiten (z.B. Auen Center sowie der Altstadt in Seewil) und Dienstleistungsangeboten in max. 2 Minuten Fahrtzeit oder in 10-15 Minuten Gehdistanz.</p></div>
  </div>
  <div class="feature" style="left:727px;top:1233px;width:240px;color:#fff">
    <svg width="24" height="24" viewBox="0 0 24 24"><circle cx="12" cy="12" r="10.5" fill="none" stroke="#fff" stroke-width="1.8"/><path d="M7 12.5l3.5 3.5 6.5-7.5" fill="none" stroke="#fff" stroke-width="2"/></svg>
    <div style="margin-left:34px"><h3 style="font-size:17px;color:#fff">Erholung im Grünen</h3><p style="font-size:12.5px">Tannried erfüllt mit seinen Wäldern, dem eigenen «Dorfberg» dem «Stürmenkopf», den offenen Feldern, den Wander- und Velorouten und der ländlichen Ruhe alle Voraussetzungen, die ein Naherholungsgebiet begehrt machen.</p></div>
  </div>

  <div class="abs" style="left:0;top:653px;width:142px;height:609px;background:var(--gray-light)"></div>
  <div class="p-head" style="top:620px">HAUS A</div>
  <div class="p-row" style="top:663px"><span class="lab">Attika Wohnung</span><span class="data"><span class="c1">4.5 Zimmer</span><span class="c2">108 m2 Wohnfläche</span><span class="c3">105 m2 grosse Sonnenterrasse</span><span class="c4">945'000 CHF</span></span></div>
  <div class="p-row" style="top:691px"><span class="lab">Obergeschoss</span><span class="data"><span class="c1">3.5 Zimmer</span><span class="c2">81 m2 Wohnfläche</span><span class="c3">16 m2 grosser Balkon</span><span class="c4">754'800 CHF</span></span></div>
  <div class="p-row" style="top:719px"><span class="lab">Obergeschoss</span><span class="data"><span class="c1">4.5 Zimmer</span><span class="c2">102 m2 Wohnfläche</span><span class="c3">33 m2 grosser Balkon</span><span class="c4">640'000 CHF</span></span></div>
  <div class="p-row" style="top:747px"><span class="lab">Erdgeschoss</span><span class="data"><span class="c1">3.5 Zimmer</span><span class="c2">81 m2 Wohnfläche</span><span class="c3">16 m2 gedeckter Sitzplatz<br>und über 120 m² Garten</span><span class="c4" style="padding-top:14px">657'000 CHF</span></span></div>
  <div class="p-row" style="top:789px"><span class="lab">Erdgeschoss</span><span class="data"><span class="c1">4.5 Zimmer</span><span class="c2">102 m2 Wohnfläche</span><span class="c3">33 m2 gedeckter Sitzplatz<br>und über 120 m² Garten</span><span class="c4" style="padding-top:14px">765'000 CHF</span></span></div>

  <div class="p-head" style="top:832px">HAUS B</div>
  <div class="p-row" style="top:874px"><span class="lab">Attika Wohnung</span><span class="data"><span class="c1">4.5 Zimmer</span><span class="c2">109 m2 Wohnfläche</span><span class="c3">107 m2 grosse Sonnenterrasse</span><span class="c4">965'000 CHF</span></span></div>
  <div class="p-row" style="top:902px"><span class="lab">Obergeschoss</span><span class="data"><span class="c1">2.5 Zimmer</span><span class="c2">69 m2 Wohnfläche</span><span class="c3">14 m2 grosse Balkon</span><span class="c4">550'000 CHF</span></span></div>
  <div class="p-row" style="top:930px"><span class="lab">Obergeschoss</span><span class="data"><span class="c1">4.5 Zimmer</span><span class="c2">117 m2 Wohnfläche</span><span class="c3">42 m2 grosse Balkon</span><span class="c4">877'500 CHF</span></span></div>
  <div class="p-row" style="top:958px"><span class="lab">Erdgeschoss</span><span class="data"><span class="c1">2.5 Zimmer</span><span class="c2">69 m2 Wohnfläche</span><span class="c3">14 m2 gedeckter Sitzplatz<br>und über 70 m² Garten</span><span class="c4" style="padding-top:14px">560'000 CHF</span></span></div>
  <div class="p-row" style="top:1000px"><span class="lab">Erdgeschoss</span><span class="data"><span class="c1">4.5 Zimmer</span><span class="c2">117 m2 Wohnfläche</span><span class="c3">42 m2 gedeckter Sitzplatz<br>und über 140 m² Garten</span><span class="c4" style="padding-top:14px">889'000 CHF</span></span></div>

  <div class="p-head" style="top:1043px">HAUS C</div>
  <div class="p-row" style="top:1084px"><span class="lab">Attika Wohnung</span><span class="data"><span class="c1">4.5 Zimmer</span><span class="c2">129 m2 Wohnfläche</span><span class="c3">132 m2 grosse Sonnenterrasse</span><span class="c4">1'125'000 CHF</span></span></div>
  <div class="p-row" style="top:1112px"><span class="lab">Obergeschoss</span><span class="data"><span class="c1">5.5 Zimmer</span><span class="c2">143 m2 Wohnfläche</span><span class="c3">43 m2 grosser Balkon</span><span class="c4">1'058'000 CHF</span></span></div>
  <div class="p-row" style="top:1140px"><span class="lab">Obergeschoss</span><span class="data"><span class="c1">3.5 Zimmer</span><span class="c2">96 m2 Wohnfläche</span><span class="c3">23 m2 grosser Balkon</span><span class="c4">730'000 CHF</span></span></div>
  <div class="p-row" style="top:1168px"><span class="lab">Erdgeschoss</span><span class="data"><span class="c1">5.5 Zimmer</span><span class="c2">143 m2 Wohnfläche</span><span class="c3">43 m2 gedeckter Sitzplatz<br>und über 120 m² Garten</span><span class="c4" style="padding-top:14px">1'065'000 CHF</span></span></div>
  <div class="p-row" style="top:1210px"><span class="lab">Erdgeschoss</span><span class="data"><span class="c1">3.5 Zimmer</span><span class="c2">96 m2 Wohnfläche</span><span class="c3">23 m2 gedeckter Sitzplatz<br>und über 60 m² Garten</span><span class="c4" style="padding-top:14px">740'000 CHF</span></span></div>

  <p class="request" style="left:40px;top:1272px;width:626px;font-size:13px;text-align:center;font-weight:600">Fordern Sie noch heute die Verkaufsunterlagen gedruckt oder per Email an.<br>Schreiben Sie uns einfach eine Chatpost mit Ihrer Adresse.</p>
  <div class="logo-name" style="left:150px;top:1320px;width:400px;font-size:27px">Brunnhofer<br>Liegenschaften AG</div>

  <div class="footer" style="width:980px;height:48px;font-size:14px;padding-left:20px">
    <span class="item" style="width:270px"><svg width="17" height="19" viewBox="0 0 13 15"><rect width="13" height="15" rx="2" fill="#fff"/><circle cx="6.5" cy="6" r="2.5" fill="#1a8be0"/></svg>Seematteweg 14, 4387 Tannried</span>
    <span class="item" style="width:140px"><svg width="17" height="17" viewBox="0 0 13 13"><rect width="13" height="13" rx="2" fill="#fff"/><path d="M3.5 3c1 3 3 5.5 6 6.5l1-1.5-2-1-1 .8c-1-.6-1.8-1.4-2.3-2.4l.8-1-1-2z" fill="#1a8be0"/></svg>079 462 37 58</span>
    <span class="item"><svg width="17" height="17" viewBox="0 0 13 13"><rect width="13" height="13" rx="2" fill="#fff"/><path d="M3 4h7v5H3zM3 4l3.5 3L10 4" fill="none" stroke="#1a8be0" stroke-width="1"/></svg>rbrunnhofer@tessin-ostwald.ch</span>
    <span class="web" style="width:274px;font-size:16.5px">www.wohnhof-am-weiher.ch</span>
  </div>
</section>

</body>
</html>
```